BrambleWorks business card

Looking for business card design that supports our company/software values. We have 2 logo designs at the moment but open to change if you think you can enhance the brand. Check out website www.brambleworks.com.au.

Target Market(s)

Education

Contact Information for Business Card

Name, title, mobile, email and website

Font styles to use
Sans Serif

Colors

Designer to choose colors to be used in the design.

Requirements
Must have
• BrambleWorks logo with tree and tagline on rear side with dark grey background colour

```html
<!DOCTYPE html>
<html lang="en">
<head>
<meta charset="utf-8">
<title>BrambleWorks business card</title>
<link rel="stylesheet" href="https://fonts.googleapis.com/css2?family=Quicksand:wght@400;500;600&display=swap">
<style>
  :root {
    --backdrop: #2b2b2e;
    --card-front: #1c1d1b;
    --card-back: #050505;
    --logo-grey: #8a8a88;
    --gold: #e3a81c;
    --muted: #8c8c8c;
    --contact: #9a9a9a;
    --divider: #3a3a3a;
    --ghost: #141414;
  }
  * { box-sizing: border-box; margin: 0; padding: 0; }
  html, body {
    width: 1200px; height: 900px; overflow: hidden;
    background: var(--backdrop);
    font-family: "Quicksand", sans-serif;
  }
  .canvas { position: relative; width: 1200px; height: 900px; }
  .card {
    position: absolute;
    width: 560px; height: 320px;
    border-radius: 3px;
    overflow: hidden;
    box-shadow: 0 18px 40px rgba(0,0,0,0.45);
  }

  /* Rear side: brand lockup */
  .card--rear { left: 70px; top: 120px; background: var(--card-front); }
  .brand-lockup {
    position: absolute; left: 50%; top: 50%;
    transform: translate(-50%, -50%);
    display: flex; align-items: center; gap: 18px;
  }
  .brand-mark {
    width: 54px; height: 54px; border-radius: 50%;
    background: var(--logo-grey);
  }
  .brand-text { display: flex; flex-direction: column; }
  .brand-name {
    font-size: 38px; font-weight: 500; color: var(--logo-grey);
    letter-spacing: 0.5px; line-height: 1;
  }
  .brand-tagline {
    margin-top: 6px; padding-top: 5px;
    border-top: 1px solid var(--logo-grey);
    font-size: 13px; font-weight: 500; color: var(--logo-grey);
    letter-spacing: 1px;
  }

  /* Front side: contact details */
  .card--contact { left: 570px; top: 470px; background: var(--card-back); }
  .ghost-name {
    position: absolute; right: -40px; bottom: -22px;
    font-size: 120px; font-weight: 400; color: var(--ghost);
    letter-spacing: 2px; line-height: 1; white-space: nowrap;
  }
  .identity {
    position: absolute; left: 48px; top: 150px;
    text-align: right; width: 190px;
  }
  .identity__name {
    font-size: 25px; font-weight: 400; color: var(--gold);
    letter-spacing: 0.5px; line-height: 1.1;
  }
  .identity__role {
    font-size: 13px; font-weight: 500; color: var(--muted);
    letter-spacing: 1.5px; margin-top: 4px;
  }
  .divider {
    position: absolute; left: 262px; top: 128px;
    width: 1px; height: 60px; background: var(--divider);
  }
  .contacts {
    position: absolute; left: 284px; top: 112px;
    list-style: none;
  }
  .contacts li {
    display: flex; align-items: center; gap: 8px;
    font-size: 13px; font-weight: 500; color: var(--contact);
    letter-spacing: 0.8px; line-height: 1; margin-bottom: 12px;
  }
  .contacts svg { width: 11px; height: 11px; flex: none; fill: var(--gold); }
</style>
</head>
<body>
<main class="canvas">

  <section class="card card--rear" aria-label="Card rear side">
    <div class="brand-lockup">
      <span class="brand-mark" aria-hidden="true"></span>
      <div class="brand-text">
        <span class="brand-name">BrambleWorks</span>
        <span class="brand-tagline">Student Success Platform</span>
      </div>
    </div>
  </section>

  <section class="card card--contact" aria-label="Card front side">
    <span class="ghost-name" aria-hidden="true">BrambleWorks</span>

    <div class="identity">
      <p class="identity__name">NAME TITLE</p>
      <p class="identity__role">DESIGNATION</p>
    </div>

    <span class="divider" aria-hidden="true"></span>

    <ul class="contacts">
      <li>
        <svg viewBox="0 0 12 12" aria-hidden="true"><path d="M1 4 C1 1.5 11 1.5 11 4 L9 5 L8 3.8 C6.8 3.4 5.2 3.4 4 3.8 L3 5 Z M3 6 H9 L10 11 H2 Z"/></svg>
        +00 0000 0000 00
      </li>
      <li>
        <svg viewBox="0 0 12 12" aria-hidden="true"><path d="M0 2 H12 V10 H0 Z M1 3 L6 7 L11 3 Z" fill-rule="evenodd"/></svg>
        sample@mail.com
      </li>
      <li>
        <svg viewBox="0 0 12 12" aria-hidden="true"><circle cx="6" cy="6" r="5.5"/></svg>
        www.brambleworks.com.au
      </li>
    </ul>
  </section>

</main>
</body>
</html>
```